Business Card Design for Vintage Jazz

I am a vintage jazz band leader in New York City. My groups play the music of the 1920s, 1930s and 1940s. My website is marlowpeskin.com for more info on what I do.

I am looking for a two sided business card design that has the look and feel of a really nice business card from the 1930s. I need to convey with the design that my work has that vintage kind of class and style, but also conveys that we are fun and entertaining.

Most importantly it should make a bold staement. If Hollis Varnum had a card, what would it have looked like? I want a card that I feel confident will make an impact and will let people know that my work is te the top that NYC has to offer in vintage jazz..

Note that I have only decided to avoid the "committed payment" option as I have not used this service before. Assuming that I get quality work I will select a design from those presented.

Target Market(s)

people who want to hire my band for events, media, and new fans of the band

Industry/Entity Type

Performing Art

Contact Information for Business Card

Definitely a matte finish, possibly a sort of old style of paper with that brown tint? definitely a thick card.

Requirements
Must have
• FRONT
• My name: Marlow Peskin
• What I do: Bandleader, Guitarist, Vocalist, Songwriter
• Contact Details: marlowpeskin.com marlow@marlowpeskin.com 646-555-0187
• BACK
• My Social Media Links:
• facebook.marlowpeskin.com
• twitter, instagram, linkedin: marlowpeskin
• I'm also including a photo image I would like to use. The photo's background is not needed, and to be honest isn't really desireable. Just looking to use the image of me.
Nice to have
• I'm attaching which could be used as is, omitted from the card, or altered maybe with text going around the outside of the circle or in some other way. It may need some clean up to the edges of the lettering as we only use it for the website thumbnail.
• If there's space I'd like to include the text "join our mailing list for a free song download: freesong.marlowpeskin.com" If not perhaps just "Download a Free Song at: freesong.marlowpeskin.com - something to this end.
Should not have
• anything cartoony. Don't think retro 90s's vision of the swing era, think actual swing era!
• anything modern. Got to look old school
• Try to avoid dark backgrounds. Since we often play in bars and clubs where it is dar, a d
• avoid script fonts.

```html
<!DOCTYPE html>
<html lang="en">
<head>
<meta charset="utf-8">
<title>Marlow Peskin – Business Card</title>
<link rel="stylesheet" href="https://fonts.googleapis.com/css2?family=Diplomata+SC&family=Cinzel:wght@700&family=Varela+Round&family=Nunito:wght@800&display=swap">
<style>
  :root {
    --paper-light: #f0cf85;
    --paper-mid: #e2b261;
    --paper-dark: #c98f43;
    --maroon: #76202f;
    --maroon-edge: #4e1019;
    --green: #3f6a12;
    --navy: #2f3f82;
    --badge-violet: #6f74b4;
    --badge-teal: #2f7f93;
    --badge-rust: #a5583a;
    --badge-fill: #f2d58f;
    --portrait-light: #d9d9d9;
    --portrait-dark: #2a2a2a;
  }
  * { margin: 0; padding: 0; box-sizing: border-box; }
  html, body { width: 1200px; height: 751px; overflow: hidden; background: #ffffff; }
  .card { position: relative; width: 1200px; height: 751px; overflow: hidden; }
  .paper-texture {
    position: absolute; inset: 0;
    background: radial-gradient(ellipse at 45% 40%, var(--paper-light) 0%, var(--paper-mid) 60%, var(--paper-dark) 100%);
  }
  .heading { position: absolute; left: 0; top: 0; width: 1200px; height: 320px; }
  .name {
    font-family: "Diplomata SC", serif; font-size: 84px;
    fill: var(--maroon); stroke: var(--maroon-edge); stroke-width: 2;
  }
  .roles { font-family: "Cinzel", serif; font-weight: 700; font-size: 40px; fill: var(--green); }
  .roles-rule { stroke: var(--green); stroke-width: 3; }
  .social-badge {
    position: absolute; border-radius: 50%;
    background: var(--badge-fill); border: 7px solid var(--badge-violet);
  }
  .social-badge--large { width: 92px; height: 92px; }
  .social-badge--small { width: 76px; height: 76px; }
  .social-badge--teal { border-color: var(--badge-teal); }
  .social-badge--rust { border-color: var(--badge-rust); }
  .social-text {
    position: absolute; font-family: "Varela Round", sans-serif; font-size: 43px;
    line-height: 1; color: var(--navy); -webkit-text-stroke: 1.2px var(--navy); white-space: nowrap;
  }
  .social-text--site { left: 346px; top: 357px; }
  .social-text--handle { left: 410px; top: 445px; }
  .mailing {
    position: absolute; left: 157px; top: 532px;
    font-family: "Nunito", sans-serif; font-weight: 800; font-size: 30px;
    line-height: 48px; color: var(--green); white-space: nowrap;
  }
  .portrait {
    position: absolute; left: 847px; top: 311px; width: 300px; height: 440px;
    border-radius: 48% 48% 50% 50% / 30% 30% 20% 20%;
    background: linear-gradient(180deg, var(--portrait-light) 0%, #8a8a8a 40%, var(--portrait-dark) 100%);
  }
</style>
</head>
<body>
<div class="card">
  <div class="paper-texture" role="img" aria-label="Aged parchment paper with faint vintage jazz instrument engraving"></div>

  <svg class="heading" viewBox="0 0 1200 320" aria-label="Marlow Peskin, Bandleader, Guitarist, Vocalist, Songwriter">
    <text class="name" x="152" y="203" textLength="882" lengthAdjust="spacingAndGlyphs">Marlow Peskin</text>
    <text class="roles" x="155" y="280" textLength="850" lengthAdjust="spacingAndGlyphs">Bandleader, Guitarist, Vocalist, Songwriter</text>
    <line class="roles-rule" x1="155" y1="288" x2="1005" y2="288"/>
  </svg>

  <span class="social-badge social-badge--large" style="left:236px; top:338px;"></span>
  <span class="social-text social-text--site">marlowpeskin.com</span>

  <span class="social-badge social-badge--small social-badge--teal" style="left:160px; top:434px;"></span>
  <span class="social-badge social-badge--small social-badge--teal" style="left:244px; top:434px;"></span>
  <span class="social-badge social-badge--small social-badge--rust" style="left:326px; top:434px;"></span>
  <span class="social-text social-text--handle">marlowpeskin</span>

  <p class="mailing">Join our mailing list for a free song download:<br>freesong.marlowpeskin.com</p>

  <div class="portrait" role="img" aria-label="Black and white photo of the bandleader in a striped blazer, tipping a straw boater hat"></div>
</div>
</body>
</html>
```